"Trade with Tilda" needs a funky and stylish business card

Hi my name is Tilda, I am an experienced Bidnest Prime Vendor with a 100% satisfaction rating and over 400 items sold

My business name and bidnest username is "Trade with Tilda" I sell other peoples items on Bidnest for a commission. The main items I sell are furniture and renovation/building salvage items such as used kitchens, bathrooms , window doors etc.

I will be promoting my service in real estate agent offices, storage facilities, removalists, building and renovating companies.

i believe selling on bidnest is a great way for people to recycle their used goods and salvageable materials and reduce waste and landfill.

Target Market(s)

people selling their homes, renovators, builders, downsizers

Industry/Entity Type

Real Estate

Contact Information for Business Card

Tilda Marlowe
0492716045

Logo Text

Trade with Tilda

Logo styles of interest
Wordmark Logo
Requirements
Must have
• the business card must feature the bidnest logo mentioning primevendorr gold ranked vendor I have attached a copy
Nice to have
• i would like to have the trade with tilda logo written in royal blue

```html
<!DOCTYPE html>
<html lang="en">
<head>
<meta charset="utf-8">
<title>Trade with Tilda – Business Card</title>
<link rel="stylesheet" href="https://fonts.googleapis.com/css2?family=Tinos:ital,wght@0,400;0,700;1,400&display=swap">
<style>
  :root {
    --page-bg: #ffffff;
    --wood-light: #c8945f;
    --wood-mid: #a5683c;
    --wood-dark: #6e3f22;
    --royal-navy: #2f3a8c;
    --ink-blue: #3a4597;
    --seal-gold: #f2b632;
    --marketplace-red: #d93a2b;
  }
  html, body {
    margin: 0;
    padding: 0;
    width: 1200px;
    height: 693px;
    overflow: hidden;
    background: var(--page-bg);
  }
  .canvas {
    position: relative;
    width: 1200px;
    height: 693px;
    background: var(--page-bg);
  }
  .card {
    position: absolute;
    left: 45px;
    top: 48px;
    width: 1116px;
    height: 602px;
    overflow: hidden;
  }
  .card__backdrop {
    position: absolute;
    inset: 0;
    background:
      linear-gradient(135deg, var(--wood-mid) 0%, var(--wood-light) 45%, var(--wood-mid) 70%, var(--wood-dark) 100%);
  }
  .badge-seal {
    position: absolute;
    left: 11px;
    top: 232px;
    width: 100px;
    height: 100px;
    border-radius: 50%;
    background: var(--seal-gold);
  }
  .vendor-mark {
    position: absolute;
    left: 117px;
    top: 244px;
    font-family: "Tinos", "Times New Roman", serif;
    font-weight: 700;
    font-size: 24px;
    line-height: 1;
    color: var(--marketplace-red);
    white-space: nowrap;
  }
  .wordmark {
    position: absolute;
    left: 123px;
    top: 296px;
    margin: 0;
    font-family: "Tinos", "Times New Roman", serif;
    font-weight: 700;
    font-size: 58px;
    line-height: 1.1;
    color: var(--royal-navy);
    white-space: nowrap;
  }
  .divider {
    position: absolute;
    left: 622px;
    top: 117px;
    width: 14px;
    height: 356px;
    background: var(--royal-navy);
  }
  .contact {
    position: absolute;
    left: 662px;
    top: 228px;
    margin: 0;
    font-family: "Tinos", "Times New Roman", serif;
    font-style: italic;
    font-size: 42px;
    line-height: 72px;
    color: var(--ink-blue);
    white-space: nowrap;
  }
  .contact p { margin: 0; }
</style>
</head>
<body>
<div class="canvas">
  <section class="card">
    <div class="card__backdrop" role="img" aria-label="Photograph of a woven wooden lattice in warm brown timber tones"></div>

    <div class="badge-seal" role="img" aria-label="Top-rated seller badge"></div>
    <div class="vendor-mark">Bidnest Prime Vendor</div>

    <h1 class="wordmark">Trade with Tilda</h1>

    <div class="divider" role="img" aria-label="Hand-drawn vertical scribble divider"></div>

    <div class="contact">
      <p class="contact__name">Name: Tilda Marlowe</p>
      <p class="contact__phone">Phone No.: 0492716045</p>
    </div>
  </section>
</div>
</body>
</html>
```